make a fireworks website

we are manufacturer of fireworks in Asia.
we need a HD fireworks website for showing product to all world customers.
we also need an register for member system,location, forum,products..etc
I added my Logo for the company.
brightpeonyhall.com.hk

and please message me if you have
any question.
here some example of website:
http://www.lanternmoth.com/
http://www.korvelmist.com/
http://www.tindle-orbwick.co.uk/
http://www.pemberlyspark.co.uk/

```html
<!DOCTYPE html>
<html lang="en">
<head>
<meta charset="utf-8">
<title>Bright Peony Hall Forum</title>
<link rel="stylesheet" href="https://fonts.googleapis.com/css2?family=Open+Sans:wght@400;600;700&display=swap">
<style>
:root{
  --page:#ffffff;
  --header:#ececec;
  --row:#efefef;
  --ink:#555555;
  --ink-soft:#9a9a9a;
  --ink-dark:#333333;
  --link:#3d8fd6;
  --accent:#1abc9c;
  --brand:#e8465a;
  --bird:#ef6a6f;
  --badge:#e74c3c;
  --line:#dddddd;
  --c-start:#1abc9c;
  --c-post:#27ae60;
  --c-pay:#f39c12;
  --c-ext:#0b5563;
  --c-q:#c0392b;
  --c-lorem:#2c3e50;
  --n-red:#e74c3c;
  --n-green:#27ae60;
  --n-purple:#8e44ad;
  --n-blue:#2980b9;
  --footer:#efefef;
}
*{box-sizing:border-box;margin:0;padding:0}
html,body{width:756px;height:1200px;overflow:hidden}
body{font-family:"Open Sans",Arial,sans-serif;background:var(--page);color:var(--ink);position:relative}
.site-header{position:absolute;left:0;top:0;width:756px;height:54px;background:var(--header);display:flex;align-items:center}
.brand{position:absolute;left:19px;top:14px;display:flex;align-items:center;gap:6px}
.brand-dot{width:22px;height:22px;border-radius:50%;background:var(--brand)}
.brand-name{font-weight:700;font-size:13px;color:var(--brand)}
.search{position:absolute;left:208px;top:12px;width:300px;height:30px;background:#fff;border:1px solid #e2e2e2;font-size:11px;color:#aaa;padding:7px 9px}
.search-btn{position:absolute;left:524px;top:12px;width:61px;height:30px;background:var(--accent);display:flex;align-items:center;justify-content:center}
.user{position:absolute;left:613px;top:20px;font-size:13px;color:#888}
.user-avatar{position:absolute;left:700px;top:11px;width:32px;height:32px;border-radius:50%;background:var(--bird);border:2px solid #fff}
.header-sep{position:absolute;left:600px;top:14px;width:1px;height:26px;background:#d5d5d5}
.tabs{position:absolute;left:0;top:54px;width:756px;height:33px;background:#f5f5f5;border-bottom:1px solid #e4e4e4}
.tab{position:absolute;top:0;height:33px;display:flex;align-items:center;gap:6px;font-size:9.5px;font-weight:700;color:#444;text-transform:uppercase}
.tab-active{left:17px;width:122px;background:#fff;border-top:3px solid var(--accent);padding-left:14px}
.tab-follow{left:152px}
.count{background:var(--badge);color:#fff;border-radius:9px;font-size:9px;padding:1px 6px}
.main{position:absolute;left:17px;top:108px;width:536px}
.new-topic{height:36px;border:1px solid #e2e2e2;font-size:11.5px;color:#aaa;padding:10px 11px;margin-bottom:14px}
.topic{position:relative;height:69px;background:var(--row);margin-bottom:2px;padding-left:72px}
.topic.plain{background:#fff}
.avatar{position:absolute;left:12px;top:11px;width:48px;height:48px;border-radius:50%;background:var(--bird)}
.avatar.photo-a{background:linear-gradient(135deg,#6b7a4f,#c9b48a)}
.avatar.photo-b{background:linear-gradient(135deg,#f0c890,#b57b4a)}
.avatar.photo-c{background:linear-gradient(135deg,#8a6a52,#e7d6c6)}
.title{padding-top:14px;font-size:15px;font-weight:600;color:#555;line-height:18px}
.title.two{padding-top:6px;width:390px}
.meta{font-size:8.5px;color:var(--ink-soft);margin-top:2px;display:flex;align-items:center;gap:4px;white-space:nowrap}
.meta .sq{width:8px;height:8px;display:inline-block}
.meta a{color:var(--link);font-size:10px;text-decoration:none}
.meta b{color:#555;font-size:9.5px;font-weight:600}
.meta .stat{display:inline-flex;align-items:center;gap:3px;margin-left:5px;font-size:9.5px;color:#555}
.actions{position:absolute;right:20px;bottom:10px;display:flex;gap:12px}
.status{padding-top:8px;font-size:8.5px;color:#888;border-left:2px solid var(--accent);padding-left:6px;margin-top:6px;line-height:10px;padding-top:0}
.votes{position:absolute;right:20px;top:9px;font-size:8.5px;color:#888}
.sidebar{position:absolute;left:573px;top:108px;width:163px}
.side-h{font-size:8.5px;font-weight:700;color:#444;text-transform:uppercase;padding-bottom:6px;border-bottom:1px solid var(--line);margin-bottom:8px}
.stats{background:#efefef;border:1px solid #e2e2e2}
.stats div{height:41px;padding:11px 15px;border-bottom:1px solid #e2e2e2;font-size:10px;color:#777;text-transform:uppercase}
.stats div:last-child{border-bottom:0}
.stats strong{font-size:19px;color:#555;font-weight:600;margin-right:3px}
.cats{list-style:none;margin:0 0 26px}
.cats li{height:22.7px;font-size:11.5px;color:#999;display:flex;align-items:center;padding-left:23px;position:relative}
.cats li.has::before{content:"";position:absolute;left:9px;border-left:5px solid #777;border-top:4px solid transparent;border-bottom:4px solid transparent}
.cats .sq{position:absolute;right:10px;width:10px;height:10px}
.list{list-style:none;margin-bottom:24px}
.list li{font-size:10.5px;color:#999;display:flex;gap:6px;margin-bottom:5px;line-height:15px}
.num{flex:0 0 11px;height:11px;border-radius:50%;color:#fff;font-size:7.5px;text-align:center;line-height:11px;margin-top:2px}
.users li{margin-bottom:3px;flex-wrap:wrap}
.users .st{display:inline-flex;gap:3px;align-items:center;color:#555;margin-left:4px}
.tags{display:flex;flex-wrap:wrap;gap:7px 8px}
.tag{background:#eeeeee;font-size:9.5px;color:#777;padding:4px 8px}
.site-footer{position:absolute;left:0;top:1124px;width:756px;height:76px;background:var(--footer)}
.social{position:absolute;left:31px;top:32px;display:flex;gap:20px}
.social span{width:10px;height:10px;border-radius:50%;background:#888}
.foot-nav{position:absolute;left:172px;top:28px;display:flex;gap:28px;font-size:11.5px;color:#555}
</style>
</head>
<body>
<header class="site-header">
  <div class="brand"><span class="brand-dot"></span><span class="brand-name">Bright Peony Hall</span></div>
  <div class="search">Search...</div>
  <div class="search-btn"><svg width="14" height="14" viewBox="0 0 14 14"><circle cx="6" cy="6" r="4.2" fill="none" stroke="#fff" stroke-width="2"/><line x1="9" y1="9" x2="12.5" y2="12.5" stroke="#fff" stroke-width="2"/></svg></div>
  <span class="header-sep"></span>
  <div class="user">admindemo ▾</div>
  <div class="user-avatar" role="img" aria-label="Member avatar"></div>
</header>
<nav class="tabs">
  <div class="tab tab-active">✎ All posts <span class="count">100</span></div>
  <div class="tab tab-follow">+ Following</div>
</nav>

<main class="main">
  <div class="new-topic">Click here to start your new topic</div>

  <article class="topic">
    <div class="avatar" role="img" aria-label="Member avatar"></div>
    <h2 class="title">Using Quillpay for payment transactions</h2>
    <p class="meta">Updated on Dec 19, 2013 in <span class="sq" style="background:var(--c-pay)"></span>Payment Methods. <a>Last reply</a> by <b>Benjamin</b>. <span class="stat">💬 1</span><span class="stat">♥ 0</span></p>
    <div class="actions"><svg width="9" height="9"><polygon points="4.5,0 5.8,3.2 9,3.4 6.5,5.5 7.3,9 4.5,7 1.7,9 2.5,5.5 0,3.4 3.2,3.2" fill="#5b9bd5"/></svg><svg width="8" height="9"><rect x="0" y="4" width="8" height="5" fill="#5b9bd5"/><path d="M2 4V2.5a2 2 0 0 1 4 0V4" stroke="#5b9bd5" fill="none"/></svg><svg width="8" height="9"><rect x="1" y="2" width="6" height="7" fill="#5b9bd5"/><rect x="0" y="0.5" width="8" height="1" fill="#5b9bd5"/></svg></div>
  </article>

  <article class="topic plain">
    <div class="avatar photo-a" role="img" aria-label="Member profile photo"></div>
    <h2 class="title">Using Quillpay for payment transactions</h2>
    <p class="meta">Updated on Dec 19, 2013 in <span class="sq" style="background:var(--c-pay)"></span>Payment Methods. <a>Last reply</a> by <b>Benjamin</b>. <span class="stat">💬 1</span><span class="stat">♥ 0</span></p>
    <div class="actions"><svg width="9" height="9"><polygon points="4.5,0 5.8,3.2 9,3.4 6.5,5.5 7.3,9 4.5,7 1.7,9 2.5,5.5 0,3.4 3.2,3.2" fill="#5b9bd5"/></svg><svg width="8" height="9"><rect x="0" y="4" width="8" height="5" fill="#5b9bd5"/><path d="M2 4V2.5a2 2 0 0 1 4 0V4" stroke="#5b9bd5" fill="none"/></svg><svg width="8" height="9"><rect x="1" y="2" width="6" height="7" fill="#5b9bd5"/><rect x="0" y="0.5" width="8" height="1" fill="#5b9bd5"/></svg></div>
  </article>

  <article class="topic">
    <div class="avatar photo-b" role="img" aria-label="Member profile photo"></div>
    <h2 class="title">Quisque nec consectetur leo.</h2>
    <p class="meta">Updated on Dec 11, 2013 <span class="sq" style="background:var(--c-lorem)"></span>LoremDemo. <a>Last reply</a> by <b>admindemo</b> <span class="stat">💬 0</span><span class="stat">♥ 0</span></p>
    <div class="actions"><svg width="9" height="9"><polygon points="4.5,0 5.8,3.2 9,3.4 6.5,5.5 7.3,9 4.5,7 1.7,9 2.5,5.5 0,3.4 3.2,3.2" fill="#5b9bd5"/></svg><svg width="8" height="9"><rect x="0" y="4" width="8" height="5" fill="#5b9bd5"/><path d="M2 4V2.5a2 2 0 0 1 4 0V4" stroke="#5b9bd5" fill="none"/></svg><svg width="8" height="9"><rect x="1" y="2" width="6" height="7" fill="#5b9bd5"/><rect x="0" y="0.5" width="8" height="1" fill="#5b9bd5"/></svg></div>
  </article>

  <article class="topic">
    <div class="avatar" role="img" aria-label="Member avatar"></div>
    <h2 class="title">Quisque nec consectetur leo.</h2>
    <p class="meta">Updated on Dec 11, 2013 <span class="sq" style="background:var(--c-lorem)"></span>LoremDemo. <a>Last reply</a> by <b>admindemo</b> <span class="stat">💬 0</span><span class="stat">♥ 0</span></p>
    <div class="actions"><svg width="9" height="9"><polygon points="4.5,0 5.8,3.2 9,3.4 6.5,5.5 7.3,9 4.5,7 1.7,9 2.5,5.5 0,3.4 3.2,3.2" fill="#5b9bd5"/></svg><svg width="8" height="9"><rect x="0" y="4" width="8" height="5" fill="#5b9bd5"/><path d="M2 4V2.5a2 2 0 0 1 4 0V4" stroke="#5b9bd5" fill="none"/></svg><svg width="8" height="9"><rect x="1" y="2" width="6" height="7" fill="#5b9bd5"/><rect x="0" y="0.5" width="8" height="1" fill="#5b9bd5"/></svg></div>
  </article>

  <article class="topic">
    <div class="avatar" role="img" aria-label="Member avatar"></div>
    <p class="status" style="margin-top:9px">Status: Not choose yet ✎</p>
    <span class="votes">▲ 0 &nbsp;▼ 0</span>
    <h2 class="title" style="padding-top:5px">How to make job posting Category and Location required</h2>
    <p class="meta">Updated on Dec 11, 2013 <span class="sq" style="background:var(--c-q)"></span>Questions?. <a>Last reply</a> by <b>admindemo</b> <span class="stat">💬 1</span><span class="stat">♥ 0</span></p>
    <div class="actions"><svg width="9" height="9"><polygon points="4.5,0 5.8,3.2 9,3.4 6.5,5.5 7.3,9 4.5,7 1.7,9 2.5,5.5 0,3.4 3.2,3.2" fill="#5b9bd5"/></svg><svg width="8" height="9"><rect x="0" y="4" width="8" height="5" fill="#5b9bd5"/><path d="M2 4V2.5a2 2 0 0 1 4 0V4" stroke="#5b9bd5" fill="none"/></svg><svg width="8" height="9"><rect x="1" y="2" width="6" height="7" fill="#5b9bd5"/><rect x="0" y="0.5" width="8" height="1" fill="#5b9bd5"/></svg></div>
  </article>

  <article class="topic">
    <div class="avatar" role="img" aria-label="Member avatar"></div>
    <h2 class="title">Quick Setup</h2>
    <p class="meta">Updated on Oct 11, 2013 <span class="sq" style="background:var(--c-start)"></span>Getting Started. <a>Last reply</a> by <b>Jade Harbor Works</b> <span class="stat">💬 5</span><span class="stat">♥ 1</span></p>
    <div class="actions"><svg width="9" height="9"><polygon points="4.5,0 5.8,3.2 9,3.4 6.5,5.5 7.3,9 4.5,7 1.7,9 2.5,5.5 0,3.4 3.2,3.2" fill="#5b9bd5"/></svg><svg width="8" height="9"><rect x="0" y="4" width="8" height="5" fill="#5b9bd5"/><path d="M2 4V2.5a2 2 0 0 1 4 0V4" stroke="#5b9bd5" fill="none"/></svg><svg width="8" height="9"><rect x="1" y="2" width="6" height="7" fill="#5b9bd5"/><rect x="0" y="0.5" width="8" height="1" fill="#5b9bd5"/></svg></div>
  </article>

  <article class="topic">
    <div class="avatar" role="img" aria-label="Member avatar"></div>
    <h2 class="title">Quick Setup</h2>
    <p class="meta">Updated on Oct 11, 2013 <span class="sq" style="background:var(--c-start)"></span>Getting Started. <a>Last reply</a> by <b>Jade Harbor Works</b> <span class="stat">💬 5</span><span class="stat">♥ 1</span></p>
    <div class="actions"><svg width="9" height="9"><polygon points="4.5,0 5.8,3.2 9,3.4 6.5,5.5 7.3,9 4.5,7 1.7,9 2.5,5.5 0,3.4 3.2,3.2" fill="#5b9bd5"/></svg><svg width="8" height="9"><rect x="0" y="4" width="8" height="5" fill="#5b9bd5"/><path d="M2 4V2.5a2 2 0 0 1 4 0V4" stroke="#5b9bd5" fill="none"/></svg><svg width="8" height="9"><rect x="1" y="2" width="6" height="7" fill="#5b9bd5"/><rect x="0" y="0.5" width="8" height="1" fill="#5b9bd5"/></svg></div>
  </article>

  <article class="topic">
    <div class="avatar photo-c" role="img" aria-label="Member profile photo"></div>
    <h2 class="title two">Nullam volutpat, quam non lobortis elementum, ligula turpis hendrerit diam, tincidunt sem</h2>
    <p class="meta">Updated on Oct 11, 2013 <span class="sq" style="background:var(--c-lorem)"></span>LoremDemo. No reply yet <span class="stat">💬 0</span><span class="stat">♥ 0</span></p>
    <div class="actions"><svg width="9" height="9"><polygon points="4.5,0 5.8,3.2 9,3.4 6.5,5.5 7.3,9 4.5,7 1.7,9 2.5,5.5 0,3.4 3.2,3.2" fill="#5b9bd5"/></svg><svg width="8" height="9"><rect x="0" y="4" width="8" height="5" fill="#5b9bd5"/><path d="M2 4V2.5a2 2 0 0 1 4 0V4" stroke="#5b9bd5" fill="none"/></svg><svg width="8" height="9"><rect x="1" y="2" width="6" height="7" fill="#5b9bd5"/><rect x="0" y="0.5" width="8" height="1" fill="#5b9bd5"/></svg></div>
  </article>

  <article class="topic">
    <div class="avatar" role="img" aria-label="Member avatar"></div>
    <h2 class="title two">Nullam volutpat, quam non lobortis elementum, ligula turpis hendrerit diam, tincidunt sem</h2>
    <p class="meta">Updated on Oct 11, 2013 <span class="sq" style="background:var(--c-lorem)"></span>LoremDemo. No reply yet <span class="stat">💬 0</span><span class="stat">♥ 0</span></p>
    <div class="actions"><svg width="9" height="9"><polygon points="4.5,0 5.8,3.2 9,3.4 6.5,5.5 7.3,9 4.5,7 1.7,9 2.5,5.5 0,3.4 3.2,3.2" fill="#5b9bd5"/></svg><svg width="8" height="9"><rect x="0" y="4" width="8" height="5" fill="#5b9bd5"/><path d="M2 4V2.5a2 2 0 0 1 4 0V4" stroke="#5b9bd5" fill="none"/></svg><svg width="8" height="9"><rect x="1" y="2" width="6" height="7" fill="#5b9bd5"/><rect x="0" y="0.5" width="8" height="1" fill="#5b9bd5"/></svg></div>
  </article>

  <article class="topic">
    <div class="avatar" role="img" aria-label="Member avatar"></div>
    <h2 class="title two">Nullam volutpat, quam non lobortis elementum, ligula turpis hendrerit diam, tincidunt sem</h2>
    <p class="meta">Updated on Oct 11, 2013 <span class="sq" style="background:var(--c-lorem)"></span>LoremDemo. No reply yet <span class="stat">💬 0</span><span class="stat">♥ 0</span></p>
    <div class="actions"><svg width="9" height="9"><polygon points="4.5,0 5.8,3.2 9,3.4 6.5,5.5 7.3,9 4.5,7 1.7,9 2.5,5.5 0,3.4 3.2,3.2" fill="#5b9bd5"/></svg><svg width="8" height="9"><rect x="0" y="4" width="8" height="5" fill="#5b9bd5"/><path d="M2 4V2.5a2 2 0 0 1 4 0V4" stroke="#5b9bd5" fill="none"/></svg><svg width="8" height="9"><rect x="1" y="2" width="6" height="7" fill="#5b9bd5"/><rect x="0" y="0.5" width="8" height="1" fill="#5b9bd5"/></svg></div>
  </article>

  <article class="topic">
    <div class="avatar" role="img" aria-label="Member avatar"></div>
    <h2 class="title two">Nullam volutpat, quam non lobortis elementum, ligula turpis hendrerit diam, tincidunt sem</h2>
    <p class="meta">Updated on Oct 11, 2013 <span class="sq" style="background:var(--c-lorem)"></span>LoremDemo. No reply yet <span class="stat">💬 0</span><span class="stat">♥ 0</span></p>
    <div class="actions"><svg width="9" height="9"><polygon points="4.5,0 5.8,3.2 9,3.4 6.5,5.5 7.3,9 4.5,7 1.7,9 2.5,5.5 0,3.4 3.2,3.2" fill="#5b9bd5"/></svg><svg width="8" height="9"><rect x="0" y="4" width="8" height="5" fill="#5b9bd5"/><path d="M2 4V2.5a2 2 0 0 1 4 0V4" stroke="#5b9bd5" fill="none"/></svg><svg width="8" height="9"><rect x="1" y="2" width="6" height="7" fill="#5b9bd5"/><rect x="0" y="0.5" width="8" height="1" fill="#5b9bd5"/></svg></div>
  </article>

  <article class="topic">
    <div class="avatar" role="img" aria-label="Member avatar"></div>
    <h2 class="title two">Nullam volutpat, quam non lobortis elementum, ligula turpis hendrerit diam, tincidunt sem</h2>
    <p class="meta">Updated on Oct 11, 2013 <span class="sq" style="background:var(--c-lorem)"></span>LoremDemo. No reply yet <span class="stat">💬 0</span><span class="stat">♥ 0</span></p>
    <div class="actions"><svg width="9" height="9"><polygon points="4.5,0 5.8,3.2 9,3.4 6.5,5.5 7.3,9 4.5,7 1.7,9 2.5,5.5 0,3.4 3.2,3.2" fill="#5b9bd5"/></svg><svg width="8" height="9"><rect x="0" y="4" width="8" height="5" fill="#5b9bd5"/><path d="M2 4V2.5a2 2 0 0 1 4 0V4" stroke="#5b9bd5" fill="none"/></svg><svg width="8" height="9"><rect x="1" y="2" width="6" height="7" fill="#5b9bd5"/><rect x="0" y="0.5" width="8" height="1" fill="#5b9bd5"/></svg></div>
  </article>

  <article class="topic">
    <div class="avatar" role="img" aria-label="Member avatar"></div>
    <h2 class="title two">Nullam volutpat, quam non lobortis elementum, ligula turpis hendrerit diam, tincidunt sem</h2>
    <p class="meta">Updated on Oct 11, 2013 <span class="sq" style="background:var(--c-lorem)"></span>LoremDemo. No reply yet <span class="stat">💬 0</span><span class="stat">♥ 0</span></p>
    <div class="actions"><svg width="9" height="9"><polygon points="4.5,0 5.8,3.2 9,3.4 6.5,5.5 7.3,9 4.5,7 1.7,9 2.5,5.5 0,3.4 3.2,3.2" fill="#5b9bd5"/></svg><svg width="8" height="9"><rect x="0" y="4" width="8" height="5" fill="#5b9bd5"/><path d="M2 4V2.5a2 2 0 0 1 4 0V4" stroke="#5b9bd5" fill="none"/></svg><svg width="8" height="9"><rect x="1" y="2" width="6" height="7" fill="#5b9bd5"/><rect x="0" y="0.5" width="8" height="1" fill="#5b9bd5"/></svg></div>
  </article>
</main>

<aside class="sidebar">
  <h3 class="side-h">Forum statistics</h3>
  <div class="stats" style="margin-bottom:28px">
    <div><strong>80</strong> Members</div>
    <div><strong>50</strong> Threads</div>
    <div><strong>100</strong> Replies</div>
  </div>

  <h3 class="side-h">Categories</h3>
  <ul class="cats">
    <li class="has">Getting Started<span class="sq" style="background:var(--c-start)"></span></li>
    <li>Posting<span class="sq" style="background:var(--c-post)"></span></li>
    <li class="has">Payment Methods<span class="sq" style="background:var(--c-pay)"></span></li>
    <li>Extension Guide<span class="sq" style="background:var(--c-ext)"></span></li>
    <li>Questions?<span class="sq" style="background:var(--c-q)"></span></li>
    <li>LoremDemo<span class="sq" style="background:var(--c-lorem)"></span></li>
  </ul>

  <h3 class="side-h">Hot topics</h3>
  <ol class="list">
    <li><span class="num" style="background:var(--n-red)">1</span>Quick Setup</li>
    <li><span class="num" style="background:var(--n-red)">2</span>Quick Setup</li>
    <li><span class="num" style="background:var(--n-green)">3</span>Editing website infomation</li>
    <li><span class="num" style="background:var(--n-green)">4</span>Downloading and installing</li>
    <li><span class="num" style="background:var(--n-purple)">5</span>Always show company profiles</li>
    <li><span class="num" style="background:var(--n-purple)">6</span>Using Quillpay for payment transactions</li>
    <li><span class="num" style="background:var(--n-blue)">7</span>Widgets</li>
    <li><span class="num" style="background:var(--n-blue)">8</span>Using Quillpay for payment transactions</li>
  </ol>

  <h3 class="side-h">Most active users</h3>
  <ol class="list users">
    <li><span class="num" style="background:var(--n-red)">1</span>Jade Harbor Works <span class="st">💬 11 ♥ 0</span></li>
    <li><span class="num" style="background:var(--n-red)">2</span>Benjamin <span class="st">💬 7 ♥ 0</span></li>
    <li><span class="num" style="background:var(--n-green)">3</span>Phillip <span class="st">💬 6 ♥ 0</span></li>
    <li><span class="num" style="background:var(--n-green)">4</span>MEDIUM <span class="st">💬 4 ♥ 0</span></li>
    <li><span class="num" style="background:var(--n-purple)">5</span>admindemo <span class="st">💬 3 ♥ 0</span></li>
    <li><span class="num" style="background:var(--n-purple)">6</span>Tobin Marsh <span class="st">💬 2 ♥ 0</span></li>
    <li><span class="num" style="background:var(--n-blue)">7</span>Brown <span class="st">💬 2 ♥ 0</span></li>
    <li><span class="num" style="background:var(--n-blue)">8</span>Colm Ardley <span class="st">💬 1 ♥ 0</span></li>
  </ol>

  <h3 class="side-h">Forum hashtags</h3>
  <div class="tags">
    <span class="tag">tags</span><span class="tag">tags</span><span class="tag">thread</span>
    <span class="tag">tags</span><span class="tag">tags</span><span class="tag">extension</span>
    <span class="tag">users</span><span class="tag">tags</span><span class="tag">setting</span>
    <span class="tag">tags</span><span class="tag">marketing</span><span class="tag">reply</span>
  </div>
</aside>

<footer class="site-footer">
  <div class="social"><span></span><span></span><span></span><span></span></div>
  <nav class="foot-nav"><span>Home</span><span>Edit Profile</span><span>Following Threads</span></nav>
</footer>
</body>
</html>
```